Investment firm needs refreshed corporate powerpoint slides design

We need a new and refreshed powerpoint template for our corporate investment deck. We are a technology private equity group that primarily invests in fast growing software companies and we would like to reflect that in a modern and light blue / transparant / white powerpoint and fonts template. I have also attached our old investor deck as a guideline and also check out our website to get an idea of what we do and what type of companies we invested in. Please note that our website is old and so our presentation should be a refreshed "2017" modern design, not a copy / paste of our website design and graphics.
Updates

Target Market(s)

Investors such as high net worth individuals, pension funds, banks, financial advisors

Industry/Entity Type

Investment

Colors
33a6d7
85cae6
cfeae6
edf8f6
ffffff
fff3d1
86cfc6

Requirements
Must have
• We let you be creative, we trust you have seen more investment presentations before.
Nice to have
• Pre-built models, flow charts, graphs, charts, etc.
Should not have
• Fancy or edgy images, this has to be a modern, fresh and trustworthy looking powerpoint template. No stock images, if you do use stock images for background purposes please be creative! :-)

```html
<!DOCTYPE html>
<html lang="en">
<head>
<meta charset="utf-8">
<title>Arden Growth Equity – Investor Deck Template</title>
<link href="https://fonts.googleapis.com/css2?family=Open+Sans:ital,wght@0,400;0,600;0,700;1,400&display=swap" rel="stylesheet">
<style>
:root{
  --blue:#33a6d7;--blue-lt:#85cae6;--mint:#86cfc6;--mint-lt:#cfeae6;--pale:#edf8f6;
  --navy:#233a5c;--ink:#333;--grey:#8a8f96;--line:#d6dde3;--bg:#e9ecef;--cell:#e6edf4;
}
*{box-sizing:border-box;margin:0;padding:0}
html,body{width:954px;height:1200px;overflow:hidden;background:var(--bg)}
body{position:relative;font-family:'Open Sans',sans-serif;color:var(--ink)}
.slide{position:absolute;width:296px;height:222px;background:#fff;box-shadow:0 1px 3px rgba(0,0,0,.25);overflow:hidden}
.c1{left:14px}.c2{left:327px}.c3{left:640px}
.r1{top:11px}.r2{top:250px}.r3{top:488px}.r4{top:727px}.r5{top:966px}
.abs{position:absolute}
.sub{position:absolute;left:16px;top:4px;font-size:5px;font-style:italic;color:#9aa0a6}
.ttl{position:absolute;left:16px;top:12px;font-size:6.4px;font-weight:700;color:#1d1d1d;white-space:nowrap}
.num{position:absolute;right:18px;top:0;width:12px;height:14px;background:var(--blue);color:#fff;font-size:5px;text-align:center;padding-top:3px;clip-path:polygon(0 0,100% 0,100% 78%,50% 100%,0 78%)}
.brand{position:absolute;left:8px;bottom:4px;font-size:9px;font-weight:600;color:var(--navy);line-height:1}
.brand::before{content:"";display:inline-block;width:3px;height:3px;background:var(--navy);margin-right:3px;vertical-align:middle}
.footbar{position:absolute;right:6px;bottom:4px;display:flex;gap:7px}
.footbar span{font-size:3px;color:var(--blue)}
.footbar span::before{content:"";display:inline-block;width:3px;height:3px;border-radius:50%;background:var(--blue);margin-right:2px;vertical-align:middle}
.t4{font-size:4px;line-height:1.35;color:#555}
.blue{color:var(--blue)}
ul.ticks{list-style:none}
ul.ticks li{font-size:3.8px;line-height:1.3;color:#444;padding-left:6px;position:relative;margin-bottom:2px}
ul.ticks li::before{content:"✓";position:absolute;left:0;color:var(--blue);font-size:4px}
ul.bul{list-style:none}
ul.bul li{font-size:3.8px;line-height:1.3;color:#444;padding-left:5px;position:relative;margin-bottom:1.5px}
ul.bul li::before{content:"";position:absolute;left:0;top:1.6px;width:2px;height:2px;border-radius:50%;background:var(--blue)}
.band{position:absolute;left:0;width:296px;background:var(--blue);display:flex}
.band .col{flex:1;text-align:center;color:#fff;font-size:3.6px;font-weight:700;text-transform:uppercase;padding-top:10px}
.band svg{display:block;margin:0 auto 6px}
.cover{background:var(--blue)}
.cover .photo{position:absolute;left:140px;top:0;width:156px;height:222px;clip-path:polygon(30% 0,100% 0,100% 100%,62% 100%,0 62%);background:linear-gradient(135deg,#c9b79a 0%,#e7dccb 35%,#8c8c8c 60%,#b89a72 100%)}
.cover h1{position:absolute;left:20px;top:34px;font-size:13px;font-weight:700;color:#fff}
.cover .intro{position:absolute;left:20px;top:52px;font-size:6px;font-style:italic;color:#d8efff}
.cover .for{position:absolute;left:20px;top:64px;font-size:6.5px;color:#e6f5ff}
.cover .by{position:absolute;left:20px;top:78px;font-size:6px;font-weight:700;color:#fff}
.cover .date{position:absolute;left:20px;top:107px;width:110px;height:14px;background:#fff;font-size:6px;font-weight:700;text-align:center;line-height:14px;color:#222}
.cover .ct{position:absolute;top:200px;font-size:4.4px;color:#e8f6ff}
.cover .ic{position:absolute;top:190px;width:9px;height:9px;border:1px solid #fff;border-radius:50%}
table{border-collapse:collapse}
.exits{position:absolute;left:0;top:49px;width:296px}
.exits th{background:var(--blue);color:#fff;font-size:6px;font-weight:600;height:18px}
.exits td{font-size:6px;color:#555;height:12px;border-bottom:1px solid #e2e6ea;text-align:center}
.exits td:first-child{text-align:left;padding-left:20px}
.exits .hi{color:var(--blue);font-weight:700}
.exits tr.tot td{font-weight:700;color:#222;border-bottom:1px solid #999}
.themes{position:absolute;left:0;top:30px;width:296px}
.themes th{background:var(--blue);color:#fff;font-size:3.8px;font-weight:600;height:14px;border-left:1px solid #fff}
.themes td{font-size:3.8px;color:#777;height:6.7px;text-align:right;padding-right:6px;border-bottom:1px solid #fff;background:#e9f1f7}
.themes td:first-child{text-align:left;padding-left:14px;background:#fff;color:#4a7aa3}
.themes tr.head td{background:var(--cell);font-weight:700;color:#333;height:8px}
.themes tr.tot td{background:var(--blue);color:#fff;font-weight:700}
.model{position:absolute;left:0;top:40px;width:296px}
.model th{background:var(--blue);color:#fff;font-size:6px;font-weight:600;height:12px}
.model th.e{background:#fff}
.model td{background:var(--cell);vertical-align:top;padding:3px 4px;border:1px solid #fff}
.model td.rh{background:var(--mint);color:#fff;font-size:6.5px;font-weight:700;text-align:center;vertical-align:middle;width:73px}
.model td .bul li{font-size:3.6px;color:#777}
.ph{background:var(--blue);color:#fff;font-size:4px;font-weight:700;padding:1px 3px;margin:3px 0 2px;width:130px}
.ph.m{background:var(--blue-lt)}
.ph.g{background:var(--mint)}
.photo-box{position:absolute;top:45px;width:56px;height:76px;background:linear-gradient(180deg,#f1f3f5,#c9ced3)}
.namebar{position:absolute;top:121px;width:56px;height:9px;background:var(--blue);color:#fff;font-size:3.4px;text-align:center;line-height:4px;padding-top:1px}
</style>
</head>
<body>

<section class="slide c1 r1 cover">
  <div class="photo" role="img" aria-label="Photo of a person working on a laptop at a wooden desk"></div>
  <h1>Arden Growth Equity</h1>
  <p class="intro">Introduction to Team and Track Record</p>
  <p class="for">For US Investor</p>
  <p class="by">Presented by: John Doe</p>
  <div class="date">Feb 2017</div>
  <span class="ic" style="left:48px"></span><span class="ic" style="left:114px"></span>
  <p class="ct" style="left:28px">info@halvard.example</p>
  <p class="ct" style="left:103px">1-555-0100</p>
</section>

<section class="slide c2 r1">
  <div class="num">2</div>
  <p class="sub" style="left:97px;top:47px">Place the sub header here</p>
  <p class="ttl" style="left:97px;top:55px">PRESENTATION AGENDA</p>
  <div class="abs" style="left:97px;top:64px;width:100px;border-top:1px solid #bbb"></div>
  <div class="abs" style="left:98px;top:64px;height:72px;border-left:1px solid #bbb"></div>
  <div class="abs" style="left:96px;top:134px;width:4px;height:4px;border-radius:50%;background:#888"></div>
  <ul class="bul abs" style="left:110px;top:74px">
    <li style="font-size:4.4px;margin-bottom:3px">Executive Summary</li>
    <li style="font-size:4.4px;margin-bottom:3px">Differentiated Model</li>
    <li style="font-size:4.4px;margin-bottom:3px">Track Record</li>
    <li style="font-size:4.4px;margin-bottom:3px">Summary of Terms</li>
    <li style="font-size:4.4px">Appendix</li>
  </ul>
  <svg class="abs" style="left:168px;top:95px" width="30" height="6"><line x1="0" y1="3" x2="24" y2="3" stroke="#888" stroke-width=".6" stroke-dasharray="2 1"/><path d="M24 1 L28 3 L24 5Z" fill="#333"/></svg>
  <ul class="bul abs" style="left:200px;top:82px">
    <li style="color:#999">Team and Advisory Board</li><li style="color:#999">Target Profile</li><li style="color:#999">Proprietary Company and</li><li style="color:#999">Executive Sourcing</li><li style="color:#999">Operational Focus</li>
  </ul>
  <p class="brand">Halvard</p>
  <div class="footbar"><span>web</span><span>share</span><span>post</span><span>link</span></div>
</section>

<section class="slide c3 r1">
  <div class="num">3</div>
  <p class="sub">Place the sub header here</p>
  <p class="ttl">ARDEN GROWTH EQUITY OVERVIEW</p>
  <div class="abs" style="left:33px;top:46px;width:250px;display:grid;grid-template-columns:repeat(3,81px);row-gap:12px">
    <div><p style="font-size:13px;color:var(--blue)">01</p><p style="font-size:4.4px;color:var(--blue);margin:2px 0 4px">SOME TITLE HERE</p><p class="t4" style="font-size:3.8px;width:70px">New management company and carry ownership held exclusively by the US team and advisors</p></div>
    <div><p style="font-size:13px;color:var(--blue)">02</p><p style="font-size:4.4px;color:var(--blue);margin:2px 0 4px">SOME TITLE HERE</p><p class="t4" style="font-size:3.8px;width:70px">New management company and carry ownership held exclusively by the US team and advisors</p></div>
    <div><p style="font-size:13px;color:var(--blue)">03</p><p style="font-size:4.4px;color:var(--blue);margin:2px 0 4px">SOME TITLE HERE</p><p class="t4" style="font-size:3.8px;width:70px">New management company and carry ownership held exclusively by the US team and advisors</p></div>
    <div><p style="font-size:13px;color:var(--blue)">04</p><p style="font-size:4.4px;color:var(--blue);margin:2px 0 4px">SOME TITLE HERE</p><p class="t4" style="font-size:3.8px;width:70px">New management company and carry ownership held exclusively by the US team and advisors</p></div>
    <div><p style="font-size:13px;color:var(--mint)">05</p><p style="font-size:4.4px;color:var(--blue);margin:2px 0 4px">SOME TITLE HERE</p><p class="t4" style="font-size:3.8px;width:70px">New management company and carry ownership held exclusively by the US team and advisors</p></div>
    <div><p style="font-size:13px;color:var(--blue)">06</p><p style="font-size:4.4px;color:var(--blue);margin:2px 0 4px">SOME TITLE HERE</p><p class="t4" style="font-size:3.8px;width:70px">New management company and carry ownership held exclusively by the US team and advisors</p></div>
  </div>
  <p class="brand">Halvard</p>
  <div class="footbar"><span>web</span><span>share</span><span>post</span><span>link</span></div>
</section>

<section class="slide c1 r2">
  <div class="num">4</div>
  <p class="sub">Place the sub header here</p>
  <p class="ttl">EXECUTIVE SUMMARY</p>
  <div class="band" style="top:65px;height:51px">
    <div class="col"><svg width="16" height="14" viewBox="0 0 16 14"><rect x="1" y="1" width="14" height="9" fill="none" stroke="#fff"/><path d="M3 8 L6 5 L9 7 L13 3" fill="none" stroke="#fff"/><line x1="8" y1="10" x2="8" y2="13" stroke="#fff"/></svg>Over a decade of<br>superior value creation</div>
    <div class="col"><svg width="16" height="14" viewBox="0 0 16 14"><path d="M2 6 H5 V13 H2Z M5 6 L8 1 Q10 1 9 5 H14 Q15 6 14 8 L12 13 H5" fill="none" stroke="#fff"/></svg>Achieving superior<br>returns</div>
    <div class="col"><svg width="16" height="14" viewBox="0 0 16 14"><path d="M2 5 H13 L10 2 M14 9 H3 L6 12" fill="none" stroke="#fff" stroke-width="1.3"/></svg>Repeatable sourcing<br>model</div>
    <div class="col"><svg width="16" height="14" viewBox="0 0 16 14"><circle cx="6" cy="4" r="3" fill="none" stroke="#fff"/><path d="M1 13 Q6 6 11 13" fill="none" stroke="#fff"/><path d="M10 8 L12 10 L15 5" fill="none" stroke="#fff"/></svg>Building successful<br>businesses</div>
  </div>
  <div class="abs" style="left:10px;top:128px;width:280px;display:flex;gap:8px">
    <ul class="ticks" style="flex:1"><li>Proven, capital efficient Executive CEO/ Founders help source and develop companies</li><li>Work closely with teams to create high value outcomes</li></ul>
    <ul class="ticks" style="flex:1"><li>Proven, capital efficient Executive CEO/ Founders help source and develop companies</li><li>Work closely with teams to create high value outcomes</li></ul>
    <ul class="ticks" style="flex:1"><li>Proven, capital efficient Executive CEO/ Founders help source and develop companies</li><li>Work closely with teams to create high value outcomes</li></ul>
    <ul class="ticks" style="flex:1"><li>Proven, capital efficient Executive CEO/ Founders help source and develop companies</li><li>Work closely with teams to create high value outcomes</li></ul>
  </div>
  <p class="brand">Halvard</p>
  <div class="footbar"><span>web</span><span>share</span><span>post</span><span>link</span></div>
</section>

<section class="slide c2 r2">
  <div class="num">5</div>
  <p class="sub">Place the sub header here</p>
  <p class="ttl">ACHIEVING SUPERIOR RETURNS</p>
  <p class="abs" style="left:17px;top:28px;font-size:5.4px;color:#333">US High Growth Buyout/Equity Portfolio 2004 through June 2016</p>
  <p class="abs blue" style="left:17px;top:35px;font-size:3.6px;font-style:italic">(Adjusted for recent sale announced June 2016)</p>
  <p class="abs" style="left:45px;top:63px;font-size:5px;font-weight:700">Halvard US Growth Returns</p>
  <p class="abs" style="left:70px;top:72px;font-size:4px"><span style="display:inline-block;width:3px;height:3px;background:var(--blue);margin-right:2px"></span>Unrealized</p>
  <svg class="abs" style="left:20px;top:80px" width="160" height="92" viewBox="0 0 160 92">
    <g stroke="#e3e3e3" stroke-width=".5"><line x1="0" y1="8" x2="160" y2="8"/><line x1="0" y1="26" x2="160" y2="26"/><line x1="0" y1="44" x2="160" y2="44"/><line x1="0" y1="62" x2="160" y2="62"/></g>
    <rect x="18" y="46" width="32" height="36" fill="var(--blue)"/>
    <rect x="90" y="27" width="32" height="55" fill="var(--blue)"/>
    <polyline points="18,46 50,46 90,27" fill="none" stroke="#333" stroke-width=".7"/>
    <line x1="0" y1="82" x2="160" y2="82" stroke="#999" stroke-width=".5"/>
    <text x="22" y="90" font-size="4.5" fill="#333">Invested</text><text x="92" y="90" font-size="4.5" fill="#333">Total Value</text>
  </svg>
  <div class="abs" style="left:204px;top:48px;width:80px">
    <p style="font-size:11px;color:var(--blue)">01</p><p style="font-size:4.2px;color:var(--blue);margin:1px 0 3px">SOME TITLE HERE</p>
    <p class="t4">1. Lorem ipsum dolor sit<br>2. diam donec neque nisl<br>3. ante rutrum proin cras<br>4. amet nunc dolor</p>
    <p style="font-size:11px;color:var(--mint);margin-top:8px">02</p><p style="font-size:4.2px;color:var(--blue);margin:1px 0 3px">SOME TITLE HERE</p>
    <p class="t4">1. Lorem ipsum dolor sit<br>2. diam donec neque nisl<br>3. ante rutrum proin cras<br>4. amet nunc dolor</p>
  </div>
  <p class="abs" style="left:30px;top:182px;width:250px;font-size:2.6px;line-height:1.3;color:#777;font-style:italic">Results shown are gross of fees and carry for the growth portfolio since inception. Past performance does not guarantee future results. Unrealized value reflects current fair market estimates as of June 30, 2016, adjusted for sale proceeds announced during the period.</p>
  <p class="brand">Halvard</p>
  <div class="footbar"><span>web</span><span>share</span><span>post</span><span>link</span></div>
</section>

<section class="slide c3 r2">
  <div class="num">6</div>
  <p class="sub">Place the sub header here</p>
  <p class="ttl">LOWER MIDDLE MARKET PROVIDES THE MAJORITY OF TECH EXITS...</p>
  <table class="exits">
    <tr><th style="text-align:left;padding-left:20px;width:105px">Exit Range</th><th>Total Deals</th><th style="width:80px">%</th></tr>
    <tr><td>$500M+</td><td>150</td><td>8%</td></tr>
    <tr><td>$300-500M</td><td>141</td><td>8%</td></tr>
    <tr><td>$150-300M</td><td>272</td><td class="hi">15%</td></tr>
    <tr><td>$50-150M</td><td>568</td><td class="hi">32%</td></tr>
    <tr><td>$20-50M</td><td>661</td><td>37%</td></tr>
    <tr class="tot"><td>TOTALS</td><td>1792</td><td>100%</td></tr>
  </table>
  <div class="abs" style="left:33px;top:157px;width:250px;display:flex;gap:14px">
    <div style="flex:1"><p style="font-size:4.2px;color:var(--blue);margin-bottom:4px">SOME TITLE HERE</p><p class="t4">Lorem ipsum dolor sit amet, diam donec neque nisl nibh, ante rutrum proin cras dui ac cum.</p></div>
    <div style="flex:1"><p style="font-size:4.2px;color:var(--blue);margin-bottom:4px">SOME TITLE HERE</p><p class="t4">Lorem ipsum dolor sit amet, diam donec neque nisl nibh, ante rutrum proin cras dui ac cum.</p></div>
    <div style="flex:1"><p style="font-size:4.2px;color:var(--blue);margin-bottom:4px">SOME TITLE HERE</p><p class="t4">Lorem ipsum dolor sit amet, diam donec neque nisl nibh, ante rutrum proin cras dui ac cum.</p></div>
  </div>
  <p class="brand">Halvard</p>
  <div class="footbar"><span>web</span><span>share</span><span>post</span><span>link</span></div>
</section>

<section class="slide c1 r3">
  <div class="num">7</div>
  <p class="sub">Place the sub header here</p>
  <p class="ttl">LOWER MIDDLE MARKET OFFERS HIGH VALUE CREATION FOR GROWTH</p>
  <svg class="abs" style="left:0;top:48px" width="296" height="100" viewBox="0 0 296 100">
    <g font-size="4" fill="#555" text-anchor="end">
      <text x="36" y="8">$80</text><text x="36" y="18">$70</text><text x="36" y="28">$60</text><text x="36" y="38">$50</text><text x="36" y="48">$40</text><text x="36" y="58">$30</text><text x="36" y="68">$20</text><text x="36" y="78">$10</text><text x="36" y="88">$0</text>
    </g>
    <line x1="40" y1="6" x2="40" y2="87" stroke="#999" stroke-width=".5"/>
    <line x1="40" y1="87" x2="280" y2="87" stroke="#999" stroke-width=".5"/>
    <g stroke="#ccc" stroke-width=".4"><line x1="108" y1="6" x2="108" y2="87"/><line x1="168" y1="6" x2="168" y2="87"/><line x1="228" y1="6" x2="228" y2="87"/></g>
    <g font-size="4" fill="#555" text-anchor="middle"><text x="63" y="95">2014</text><text x="125" y="95">2015</text><text x="185" y="95">2016</text><text x="248" y="95">2017</text></g>
    <circle cx="63" cy="66" r="11" fill="var(--blue)"/><text x="63" y="68" font-size="5" fill="#fff" font-weight="700" text-anchor="middle">$22M</text>
    <circle cx="125" cy="34" r="13" fill="#c9bf9a"/><text x="125" y="36" font-size="5" fill="#fff" font-weight="700" text-anchor="middle">$54M</text>
    <circle cx="185" cy="25" r="13" fill="var(--mint)"/><text x="185" y="27" font-size="5" fill="#fff" font-weight="700" text-anchor="middle">$60M</text>
    <circle cx="248" cy="16" r="13" fill="var(--blue)"/><text x="248" y="18" font-size="5" fill="#fff" font-weight="700" text-anchor="middle">$70M</text>
    <rect x="44" y="78" width="4" height="4" fill="#666"/><text x="50" y="82" font-size="5" font-weight="700" fill="#444">Northwire</text>
    <rect x="112" y="57" width="3" height="3" fill="#777"/><text x="117" y="60" font-size="4.2" fill="#777">Vantalo</text>
    <rect x="168" y="41" width="3" height="3" fill="#777"/><text x="173" y="44" font-size="4.2" fill="#777">Meridio</text>
    <rect x="230" y="32" width="3" height="3" fill="#777"/><text x="235" y="35" font-size="4.6" fill="#777">Quillon</text>
  </svg>
  <p class="abs" style="left:44px;top:162px;width:210px;text-align:center;background:var(--mint-lt);font-size:6px;color:#555;height:9px;line-height:9px">EXIT VALUES</p>
  <div class="abs" style="left:44px;top:172px;width:210px;height:9px;background:#8f9499;display:flex;font-size:4.8px;color:#fff;line-height:9px;text-align:center">
    <span style="flex:1">$165M</span><span style="flex:1">$250M/$500M*</span><span style="flex:1">$400M</span><span style="flex:1">$98M</span>
  </div>
  <p class="brand">Halvard</p>
  <div class="footbar"><span>web</span><span>share</span><span>post</span><span>link</span></div>
</section>

<section class="slide c2 r3">
  <div class="num">8</div>
  <p class="sub">Place the sub header here</p>
  <p class="ttl">DIFFERENTIATED MODEL: FOUR PILLARS FOR SUCCESS</p>
  <div class="band" style="top:64px;height:48px">
    <div class="col"><svg width="16" height="14" viewBox="0 0 16 14"><circle cx="8" cy="3" r="2" fill="#fff"/><circle cx="3" cy="5" r="1.6" fill="#fff"/><circle cx="13" cy="5" r="1.6" fill="#fff"/><rect x="6" y="6" width="4" height="7" fill="#fff"/><rect x="1.5" y="7.5" width="3" height="5" fill="#fff"/><rect x="11.5" y="7.5" width="3" height="5" fill="#fff"/></svg>Team and Advisory<br>Board</div>
    <div class="col"><svg width="16" height="14" viewBox="0 0 16 14"><circle cx="7" cy="7" r="6" fill="none" stroke="#fff" stroke-width="1.3"/><circle cx="7" cy="7" r="3" fill="none" stroke="#fff"/><path d="M7 7 L14 1" stroke="#fff" stroke-width="1.3"/></svg>Target Profile</div>
    <div class="col"><svg width="16" height="14" viewBox="0 0 16 14"><circle cx="8" cy="3" r="2.5" fill="#fff"/><path d="M3 14 V9 Q8 5 13 9 V14Z" fill="#fff"/></svg>Proprietary Company /<br>Executive Sourcing</div>
    <div class="col"><svg width="16" height="14" viewBox="0 0 16 14"><circle cx="9" cy="6" r="5" fill="none" stroke="#fff" stroke-width="1.3"/><line x1="5" y1="10" x2="1" y2="14" stroke="#fff" stroke-width="1.6"/></svg>Operational Focus</div>
  </div>
  <div class="abs" style="left:12px;top:124px;width:280px;display:flex;gap:8px">
    <ul class="bul" style="flex:1"><li>Team with strong investment and technology backgrounds</li><li>Executive &amp; board recruitment from Executive Advisory Board:</li><li style="margin-left:4px">Proven Founders/CEOs with capital efficient, high value exits</li></ul>
    <ul class="bul" style="flex:1"><li>Growth buyouts / significant minority</li><li>Recurring revenue of $5M to $50M with revenue growth of 20% to 100%+</li><li>Capital efficient businesses with significant ownership by founder</li></ul>
    <ul class="bul" style="flex:1"><li>Algorithmic approach evaluates 100K companies every 8 weeks</li><li>Companies screened for themes, predicted financials, team profile</li><li>Regional high value events with Executive Advisory Board members</li></ul>
    <ul class="bul" style="flex:1"><li>Team building/ Operational focus creates strong alpha</li><li>Control investments enable rapid team development; unique for high growth, small tech companies</li><li>Price disciplined on investment, target 3x return at reasonable outcomes</li></ul>
  </div>
  <p class="brand">Halvard</p>
  <div class="footbar"><span>web</span><span>share</span><span>post</span><span>link</span></div>
</section>

<section class="slide c3 r3">
  <div class="num">9</div>
  <p class="sub">Place the sub header here</p>
  <p class="ttl">DIFFERENTIATED MODEL: FOUR PILLARS FOR SUCCESS</p>
  <svg class="abs" style="left:6px;top:62px" width="118" height="118" viewBox="0 0 122 122">
    <path d="M59 59 L59 0 A59 59 0 0 0 0 59Z" fill="var(--blue)"/>
    <path d="M63 59 L63 0 A59 59 0 0 1 122 59Z" fill="#3d7fc7"/>
    <path d="M59 63 L0 63 A59 59 0 0 0 59 122Z" fill="#8fb0d8"/>
    <path d="M63 63 L122 63 A59 59 0 0 1 63 122Z" fill="var(--mint)"/>
    <circle cx="61" cy="61" r="12" fill="none" stroke="#fff" stroke-width="1.5"/>
    <g fill="#fff" font-size="4" text-anchor="middle"><text x="32" y="44">Team and</text><text x="32" y="49">Advisory Board</text><text x="92" y="45">Target Profile</text><text x="30" y="89">Operational</text><text x="30" y="94">Focus</text><text x="92" y="87">Proprietary</text><text x="92" y="92">Company and</text><text x="92" y="97">Executive</text><text x="92" y="102">Sourcing</text></g>
    <g fill="none" stroke="#fff" stroke-width=".8"><circle cx="32" cy="30" r="4"/><circle cx="92" cy="30" r="4"/><circle cx="30" cy="76" r="4"/><circle cx="92" cy="74" r="4"/></g>
  </svg>
  <div class="abs" style="left:137px;top:40px;width:152px">
    <p class="ph">Team and Advisory Board</p>
    <ul class="bul"><li>Sam Ortell was identified through our proprietary executive sourcing model</li><li>As CEO, Sam delivered 10x+ returns to investors twice (2002 Software and Relaydesk)</li><li>We spent a year reviewing deals</li><li>Improved leverage through channel experience and local network</li></ul>
    <p class="ph m">Operational Focus</p>
    <ul class="bul"><li>Sam had multiple offers – We provided a differentiated compensation package and co-investment opportunity</li><li>Sam recruited several executives from previous teams he led</li></ul>
    <p class="ph">Target Profile</p>
    <ul class="bul"><li>Transaction was a growth buyout – founders wanted to sell majority</li><li>Portfolio investment had proven category relevance and ecosystem experience</li><li>Strong recurring revenue / SaaS metrics</li></ul>
    <p class="ph g">Proprietary Company / Executive Sourcing</p>
    <ul class="bul"><li>Proactive outreach; company was sourced via our Predictive Model</li><li>We introduced Sam to the initial discovery calls to assist with diligence and to highlight him as a potential advisor</li><li>The company had engaged with a banker and was expecting term sheets</li></ul>
  </div>
  <p class="brand">Halvard</p>
  <div class="footbar"><span>web</span><span>share</span><span>post</span><span>link</span></div>
</section>

<section class="slide c1 r4">
  <div class="num">10</div>
  <p class="sub">Place the sub header here</p>
  <p class="ttl">TEAM: INVESTORS</p>
  <div class="photo-box" style="left:4px" role="img" aria-label="Portrait photo of team member"></div>
  <div class="photo-box" style="left:62px" role="img" aria-label="Portrait photo of team member"></div>
  <div class="photo-box" style="left:120px" role="img" aria-label="Portrait photo of team member"></div>
  <div class="photo-box" style="left:178px" role="img" aria-label="Portrait photo of team member"></div>
  <div class="photo-box" style="left:236px" role="img" aria-label="Portrait photo of team member"></div>
  <div class="namebar" style="left:4px">Avery Lorne<br>Partner</div>
  <div class="namebar" style="left:62px">Blake Hunt<br>Partner</div>
  <div class="namebar" style="left:120px">Casey Rowe<br>Finance Director</div>
  <div class="namebar" style="left:178px">Drew Ellis<br>Principal</div>
  <div class="namebar" style="left:236px">Emery Marsh<br>Associate</div>
  <div class="abs" style="left:6px;top:134px;width:288px;display:flex;gap:4px">
    <ul class="bul" style="flex:1"><li>Joined in 2000</li><li>20 years investment banking and technology experience</li><li>M&amp;A advisor, specializing in high-growth companies</li><li>MBA, BS university</li></ul>
    <ul class="bul" style="flex:1"><li>Joined in 2000</li><li>21 years investment banking and technology experience</li><li>Product Marketing Engineer at a chipmaker</li><li>BS Degree, university</li></ul>
    <ul class="bul" style="flex:1"><li>Joined in 2012</li><li>Financial Controller, Partners, Board Capital</li><li>Chartered Accountant at an accounting firm</li><li>BSc in Biochemistry</li></ul>
    <ul class="bul" style="flex:1"><li>Joined in 2007</li><li>Leads Deal Sourcing and Investment Review Process</li><li>Data analytics/mining specialist</li><li>BA degree, university</li></ul>
    <ul class="bul" style="flex:1"><li>Joined in 2014</li><li>Capital Partners Analyst</li><li>BA, university</li><li>MS in Corporate Finance, Business School</li></ul>
  </div>
  <p class="brand">Halvard</p>
  <div class="footbar"><span>web</span><span>share</span><span>post</span><span>link</span></div>
</section>

<section class="slide c2 r4">
  <div class="num">11</div>
  <p class="sub">Place the sub header here</p>
  <p class="ttl">GROWTH BUYOUTS: ATTRACTIVE INVESTMENTS REQUIRING UNIQUE EXPERTISE</p>
  <p class="abs t4" style="left:16px;top:40px;width:262px;color:#777">Contrary to popular belief, Lorem Ipsum is not simply random text. It has roots in a piece of classical Latin literature from 45 BC. Contrary to popular belief, Lorem Ipsum is not simply random text. It has roots in a piece of classical Latin literature from 45 BC.</p>
  <svg class="abs" style="left:0;top:74px" width="296" height="80" viewBox="0 0 296 80">
    <path d="M20 4 H262 V0 L272 8 L262 16 V12 H20Z" fill="var(--blue)"/>
    <path d="M80 20 H262 V16 L272 24 L262 32 V28 H80Z" fill="var(--blue-lt)"/>
    <path d="M150 36 H262 V32 L272 40 L262 48 V44 H150Z" fill="var(--mint)"/>
    <path d="M190 52 H262 V48 L272 56 L262 64 V60 H190Z" fill="#a9d6e8"/>
    <g fill="#fff" font-size="4.2"><text x="40" y="10">Growth buyouts: Require Skills and Experience</text><text x="95" y="26">Differ from traditional buyouts</text><text x="165" y="42">Growth buyouts play to our strengths</text><text x="205" y="55.5" font-size="3.4">Attractive alternative to</text><text x="205" y="59.5" font-size="3.4">leveraged buyouts</text></g>
    <rect x="22" y="2" width="10" height="10" fill="#fff" opacity=".4"/>
  </svg>
  <p class="abs t4 blue" style="left:24px;top:96px;width:50px;font-size:3.4px">Contrary to popular belief, Lorem Ipsum is not simply random text. It has roots in a piece of classical Latin literature from 45 BC.</p>
  <p class="abs t4 blue" style="left:82px;top:110px;width:50px;font-size:3.4px">Contrary to popular belief, Lorem Ipsum is not simply random text. It has roots in a piece of classical Latin literature from 45 BC.</p>
  <p class="abs t4 blue" style="left:138px;top:126px;width:50px;font-size:3.4px">Contrary to popular belief, Lorem Ipsum is not simply random text. It has roots in a piece of classical Latin literature from 45 BC.</p>
  <p class="abs t4 blue" style="left:193px;top:142px;width:50px;font-size:3.4px">Contrary to popular belief, Lorem Ipsum is not simply random text. It has roots in a piece of classical Latin literature from 45 BC.</p>
  <p class="brand">Halvard</p>
  <div class="footbar"><span>web</span><span>share</span><span>post</span><span>link</span></div>
</section>

<section class="slide c3 r4">
  <div class="num">12</div>
  <p class="sub">Place the sub header here</p>
  <p class="ttl">TOP 1000 PROSPECTS BY THEME / GROWTH RATE</p>
  <table class="themes">
    <tr><th style="background:#fff;width:113px"></th><th>Revenue Estimate 15'</th><th>Average Growth 15'</th><th>% of Top Prospects</th></tr>
    <tr class="head"><td>THEME</td><td></td><td></td><td></td></tr>
    <tr><td>Security</td><td>7.2</td><td>145%</td><td>2%</td></tr>
    <tr><td>Healthcare</td><td>7.0</td><td>77%</td><td>7%</td></tr>
    <tr><td>Mobile</td><td>5.7</td><td>72%</td><td>9%</td></tr>
    <tr><td>Other</td><td>6.1</td><td>69%</td><td>7%</td></tr>
    <tr><td>E-commerce</td><td>5.8</td><td>65%</td><td>4%</td></tr>
    <tr><td>Consumer</td><td>4.9</td><td>62%</td><td>6%</td></tr>
    <tr><td>Education</td><td>6.2</td><td>59%</td><td>2%</td></tr>
    <tr><td>Cloud and System Software</td><td>7.2</td><td>59%</td><td>3%</td></tr>
    <tr><td>Adtech</td><td>9.6</td><td>58%</td><td>3%</td></tr>
    <tr><td>Software</td><td>5.9</td><td>57%</td><td>28%</td></tr>
    <tr><td>Data Analytics</td><td>5.4</td><td>56%</td><td>15%</td></tr>
    <tr><td>Financial</td><td>6.3</td><td>51%</td><td>4%</td></tr>
    <tr><td>Services</td><td>7.8</td><td>50%</td><td>6%</td></tr>
    <tr><td>Hardware</td><td>4.9</td><td>27%</td><td>1%</td></tr>
    <tr class="tot"><td style="background:var(--blue);color:#fff">Total</td><td>6.1</td><td>62%</td><td>100%</td></tr>
  </table>
  <p class="brand">Halvard</p>
  <div class="footbar"><span>web</span><span>share</span><span>post</span><span>link</span></div>
</section>

<section class="slide c1 r5">
  <div class="num">13</div>
  <p class="sub">Place the sub header here</p>
  <p class="ttl">AG GROWTH'S EXECUTION MODEL</p>
  <table class="model">
    <tr><th class="e"></th><th>Investment</th><th>Execution</th><th>Exit</th></tr>
    <tr style="height:46px"><td class="rh">Company</td>
      <td><ul class="bul"><li>$5-50M revenue, 30-100%+ growth</li><li>Capital efficient</li></ul></td>
      <td><ul class="bul"><li>Scale revenue 3-10x</li><li>Professionalize the organization</li><li>EBITDA cost rate &gt; 25% revenue</li></ul></td>
      <td><ul class="bul"><li>Maintain 30%+ revenue growth</li><li>#1 or 2 in its market</li><li>Attractive SaaS Metrics</li></ul></td></tr>
    <tr style="height:48px"><td class="rh">AG Growth</td>
      <td><ul class="bul"><li>$15M to $25M primary / secondary</li><li>Control / significant minority</li><li>Secure venture debt for incremental working capital</li></ul></td>
      <td><ul class="bul"><li>Sales and Marketing effectiveness</li><li>Strategy and positioning for maximum value</li><li>Recruiting and founder transition</li><li>Exit planning/execution</li></ul></td>
      <td><ul class="bul"><li>Achieve 3x at $75-$150M exit</li><li>Downside protection</li><li>10x upside potential</li></ul></td></tr>
    <tr style="height:42px"><td class="rh">Executive</td>
      <td><ul class="bul"><li>Add CEO / Executive Chairman / Board</li><li>Co-invest $500k to $2M</li></ul></td>
      <td><ul class="bul"><li>Prior Experience</li><li>Well-pack / Recruit Team Members from previous companies</li><li>Relationships (investor, customer, partners)</li></ul></td>
      <td><ul class="bul"><li>Founder economics &amp; risk/ reward profile</li></ul></td></tr>
  </table>
  <p class="brand">Halvard</p>
  <div class="footbar"><span>web</span><span>share</span><span>post</span><span>link</span></div>
</section>

<section class="slide c2 r5">
  <div class="num">14</div>
  <p class="sub">Place the sub header here</p>
  <p class="ttl">EQUITY PROTECTION WITH UPSIDE OPTION</p>
  <svg class="abs" style="left:0;top:30px" width="296" height="178" viewBox="0 0 296 178">
    <line x1="24" y1="12" x2="24" y2="160" stroke="#555" stroke-width=".6"/><path d="M22 14 L24 8 L26 14Z" fill="#555"/>
    <line x1="24" y1="160" x2="290" y2="160" stroke="#555" stroke-width=".6"/>
    <g font-size="3.6" fill="#555" text-anchor="end"><text x="21" y="30">5X</text><text x="21" y="58">4X</text><text x="21" y="86">3X</text><text x="21" y="114">2X</text><text x="21" y="142">1X</text></g>
    <text x="9" y="120" font-size="4" fill="#555" transform="rotate(-90 9 120)">Investment Multiple</text>
    <path d="M45 150 V103 H118 V109 H51 V150Z" fill="var(--blue)"/>
    <path d="M128 122 V75 H205 V81 H134 V122Z" fill="var(--blue-lt)"/>
    <path d="M210 95 V50 H290 V56 H216 V95Z" fill="#a6aaae"/>
    <g font-size="4.4" font-weight="700" fill="#222"><text x="60" y="100">FINANCIAL</text><text x="140" y="72">OPERATIONAL</text><text x="225" y="47">STRATEGIC</text></g>
    <g font-size="3.6" fill="#777"><text x="54" y="126">•Preferred instrument</text><text x="54" y="131">structured to produce 1-2x</text><text x="54" y="136">return</text><text x="54" y="141">•Protected equity instrument</text>
    <text x="137" y="98">•Increase revenue growth</text><text x="137" y="104">•Expand business</text><text x="137" y="110">•Executive &amp; board</text><text x="137" y="115">recruitment</text><text x="137" y="121">•Founder transition</text>
    <text x="219" y="71">•Competitive repositioning</text><text x="219" y="77">•New innovative technology</text><text x="219" y="83">•Develop high growth markets</text><text x="219" y="89">•Acquisitions</text><text x="219" y="95">•Exit positioning and</text><text x="219" y="100">execution</text></g>
    <g font-size="3.6" fill="#555" text-anchor="middle"><text x="85" y="168">Downside</text><text x="85" y="173">Risk Protection</text><text x="185" y="168">Base Case</text><text x="185" y="173">Fundamentals</text><text x="265" y="168">Game Changing</text><text x="265" y="173">Opportunities</text></g>
  </svg>
  <p class="brand">Halvard</p>
  <div class="footbar"><span>web</span><span>share</span><span>post</span><span>link</span></div>
</section>

<section class="slide c3 r5">
  <div class="num">15</div>
  <p class="sub" style="left:97px;top:47px">Place the sub header here</p>
  <p class="ttl" style="left:97px;top:55px">CONCLUSIONS</p>
  <div class="abs" style="left:97px;top:64px;width:150px;border-top:1px solid #bbb"></div>
  <div class="abs" style="left:98px;top:64px;height:100px;border-left:1px solid #bbb"></div>
  <div class="abs" style="left:96px;top:162px;width:4px;height:4px;border-radius:50%;background:#888"></div>
  <ul class="bul abs" style="left:110px;top:78px;width:175px">
    <li style="font-size:4.6px;line-height:1.75">Cohesive team with 20+ years of working together</li>
    <li style="font-size:4.6px;line-height:1.75">Compelling opportunity in lower-middle market buyouts and growth equity in private, recurring revenue software companies</li>
    <li style="font-size:4.6px;line-height:1.75">Repeatable, proprietary, analytics-driven model for sourcing executives and investment prospects</li>
    <li style="font-size:4.6px;line-height:1.75">Proven, ability to deliver above market, risk-balanced returns of 3-5x</li>
  </ul>
  <p class="brand">Halvard</p>
  <div class="footbar"><span>web</span><span>share</span><span>post</span><span>link</span></div>
</section>

</body>
</html>
```